Stationery for Software Developer
Glen Ambrose
Project: Stationery for Software Developer
Stationery for Software Developer - Information Technology
Creative Brief
Professional
Software Engineer
Greater Seattle Area
glen@ambrosk.me
http://ambrosk.me
Chirpline: @ambrog Circlr+: +GlenAmbrose Facepage: gambrosk WorkNexus: glenambrose (Prefer Social Icons to be used instead of the names)
Main Logo with name on front. Open to variations of the main logo on front.
sevensky sevensky
gambrosk gambrosk
My apologies. I accidentally started this project before I had my logo in hand. I have contacted support about suspending this contest for 4 days until I have it. Thanks for the interest! Glen
paul1990 paul1990
Hi, Where is your logo?

```html
<!DOCTYPE html>
<html lang="en">
<head>
<meta charset="utf-8">
<title>Glen Ambrose – Business Card</title>
<link href="https://fonts.googleapis.com/css2?family=Open+Sans:wght@400;600;700&display=swap" rel="stylesheet">
<style>
  :root {
    --backdrop: #e6e6e8;
    --card: #ffffff;
    --ink: #2b2b2b;
    --title-blue: #3a74b8;
    --brand-blue: #3b4fa0;
    --accent-pink: #e4468f;
    --accent-cyan: #86d3e2;
    --icon: #3a3a3a;
    --on-accent: #ffffff;
  }
  * { margin: 0; padding: 0; box-sizing: border-box; }
  html, body {
    width: 1200px;
    height: 816px;
    overflow: hidden;
    background: var(--backdrop);
    font-family: "Open Sans", Arial, sans-serif;
  }
  .business-card {
    position: absolute;
    left: 40px;
    top: 40px;
    width: 1120px;
    height: 736px;
    background: var(--card);
    border-radius: 40px;
    overflow: hidden;
    box-shadow: 0 6px 24px rgba(0,0,0,0.12);
  }
  .holder {
    position: absolute;
    left: 80px;
    top: 228px;
  }
  .holder-name {
    font-size: 38px;
    font-weight: 700;
    color: var(--ink);
    letter-spacing: 0.5px;
    line-height: 1.1;
    text-transform: uppercase;
  }
  .holder-title {
    font-size: 28px;
    font-weight: 400;
    color: var(--title-blue);
    margin-top: 4px;
  }
  .contact-list {
    position: absolute;
    left: 84px;
    top: 372px;
    list-style: none;
    font-size: 24px;
    color: var(--ink);
    line-height: 1.3;
  }
  .contact-list li {
    display: flex;
    align-items: flex-start;
    gap: 12px;
    margin-bottom: 6px;
  }
  .contact-list .address { font-weight: 600; }
  .contact-icon {
    width: 22px;
    height: 22px;
    margin-top: 5px;
    flex: none;
    fill: var(--icon);
  }
  .brand {
    position: absolute;
    left: 560px;
    top: 352px;
    display: flex;
    align-items: center;
    gap: 22px;
  }
  .brand-mark {
    width: 58px;
    height: 58px;
    background: var(--accent-pink);
  }
  .brand-name {
    font-size: 66px;
    font-weight: 400;
    color: var(--brand-blue);
    line-height: 1;
    white-space: nowrap;
  }
  .web-band {
    position: absolute;
    left: 540px;
    right: 0;
    top: 516px;
    height: 84px;
    background: var(--accent-cyan);
    border-radius: 42px 0 0 42px;
    display: flex;
    align-items: center;
    padding-left: 48px;
  }
  .web-address {
    font-size: 34px;
    color: var(--on-accent);
    font-weight: 400;
    letter-spacing: 0.5px;
  }
  .base-band {
    position: absolute;
    left: 0;
    right: 0;
    bottom: 0;
    height: 136px;
    background: var(--accent-pink);
    display: flex;
    align-items: flex-end;
    padding: 0 80px 34px;
  }
  .social-list {
    list-style: none;
    display: flex;
    gap: 34px;
    font-size: 19px;
    color: var(--on-accent);
    white-space: nowrap;
  }
  .social-list li {
    display: flex;
    align-items: center;
    gap: 10px;
  }
  .social-dot {
    width: 14px;
    height: 14px;
    border-radius: 50%;
    background: var(--on-accent);
    flex: none;
  }
</style>
</head>
<body>
  <div class="business-card">
    <div class="holder">
      <p class="holder-name">Glen Ambrose</p>
      <p class="holder-title">Software Engineer</p>
    </div>

    <ul class="contact-list">
      <li class="address">
        <svg class="contact-icon" viewBox="0 0 24 24" aria-hidden="true"><path d="M12 2a7 7 0 0 0-7 7c0 5.2 7 13 7 13s7-7.8 7-13a7 7 0 0 0-7-7zm0 9.5A2.5 2.5 0 1 1 12 6.5a2.5 2.5 0 0 1 0 5z"/></svg>
        <span>Greater Seattle Area</span>
      </li>
      <li>
        <svg class="contact-icon" viewBox="0 0 24 24" aria-hidden="true"><path d="M6.6 10.8a15.1 15.1 0 0 0 6.6 6.6l2.2-2.2a1 1 0 0 1 1-.25 11.4 11.4 0 0 0 3.6.57 1 1 0 0 1 1 1V20a1 1 0 0 1-1 1A17 17 0 0 1 3 4a1 1 0 0 1 1-1h3.5a1 1 0 0 1 1 1c0 1.25.2 2.45.57 3.57a1 1 0 0 1-.25 1z"/></svg>
        <span>012 555 0147</span>
      </li>
      <li>
        <svg class="contact-icon" viewBox="0 0 24 24" aria-hidden="true"><path d="M8 1h8a2 2 0 0 1 2 2v18a2 2 0 0 1-2 2H8a2 2 0 0 1-2-2V3a2 2 0 0 1 2-2zm0 3v14h8V4zm4 15.2a1.1 1.1 0 1 0 0 2.2 1.1 1.1 0 0 0 0-2.2z"/></svg>
        <span>012 555 0183</span>
      </li>
      <li>
        <svg class="contact-icon" viewBox="0 0 24 24" aria-hidden="true"><path d="M3 5h18a1 1 0 0 1 1 1v12a1 1 0 0 1-1 1H3a1 1 0 0 1-1-1V6a1 1 0 0 1 1-1zm1 2.3V17h16V7.3l-8 5.2z M5 7l7 4.5L19 7z"/></svg>
        <span>glen@ambrosk.me</span>
      </li>
    </ul>

    <div class="brand">
      <span class="brand-mark" aria-hidden="true"></span>
      <span class="brand-name">Glen Ambrose</span>
    </div>

    <div class="base-band">
      <ul class="social-list">
        <li><span class="social-dot" aria-hidden="true"></span>Chirpline @ambrog</li>
        <li><span class="social-dot" aria-hidden="true"></span>Circlr+ +GlenAmbrose</li>
        <li><span class="social-dot" aria-hidden="true"></span>Facepage gambrosk</li>
        <li><span class="social-dot" aria-hidden="true"></span>WorkNexus glenambrose</li>
      </ul>
    </div>
    <div class="web-band">
      <span class="web-address">www.ambrosk.me</span>
    </div>
  </div>
</body>
</html>
```